Web Design Project Bright Lantern

I am needing a website for a theatre called Bright Lantern Stage School (blstage.com) which has already been purchsed from web nest. (Let me know if you need any other info on that.)We need a website that is professional looking and easy to access. Attached is the logo as well as the business card design. I think it would be nice to have the same type of design that’s on the business card but I am definitely open to other creative ideas. I need the website to be in a format where I can edit it in the future when I need to add classes and events to it. Also, some other things I need are I need are a…
A homepage. On the homepage we would like the motto, “Rise to the spotlight.” Also, the mission statement,
Bright Lantern Stage School strives to help students achieve excellence in performance, while building self-confidence and creativity. The Bright Lantern Stage School has created a fun and safe environment, where students can learn, acquire new skills, and explore their potential through musical theatre. Students not only have the freedom to, but are encouraged to embrace who they are and can lose their fear of judgment from others.
Class Registration Page for the classes- (As well as a coin link option for each if that is possible)
4-6 Musical Theatre
Tuesday’s 4:00PM-5:00PM
January 6th – February 24th
8 Weeks
Cost $160
Curriculum: Moss Harbor
Class info: In MT 4-6 your students will learn the basics of singing, dancing, and acting. A lesson of theatre terminology or technique will be taught each week as well as working on the show that will be performed at the end of the 8 weeks semester.

6-9 Musical Theatre
Tuesday’s 5:15PM-6:45PM
January 6th- February 24th
8 Weeks
Cost: $200
Curriculum: Tilly
Class info: In MT 6-9 your students will learn the basics of singing, dancing, and acting. A lesson of theatre terminology or technique will be taught each week as well as working on the show that will be performed at the end of the 8 weeks semester.
9-12 Musical Theatre
Wednesday’s 5:00-7:00PM
8 Weeks
Cost: $240
Curriculum: Gilded
Class info: In MT 9-12 your students will learn intermediate levels of singing, dancing, and acting. A lesson of theatre terminology or technique will be taught each week as well as working on the show that will be performed at the end of the 8 weeks semester.

About- (Include headshot that is attached)
A native Coloradan, Maren is an actress, director, teacher, and wife. She was a Dean’s List graduate of Northridge College in Florida, she holds a B.S. degree in Theatre. Her Capstone Project involved writing, producing, directing, and starring in a 60-minute one-woman musical which was noted by the Chairman of Theatre as setting new standard for the NRC project. Initially attending Harmon College, Maren was one of nine students representing HC at the Great Plains Drama Festival. Maren has also been a senior theatre director at the Maplewood Youth Playhouse for 4 years, where she directed fall, spring, and summer classes for ages 4-19. Her experience includes directing the main stage production, Quill Jr., assistant director for, Keep Your Chin Up Milo Barnes, and stage management for Der Nachtvogel.

Contact us
Phone: 303-555-0147
Email: blstageschool.com

Also, I do not have any photos of students yet so it's ok if their aren't many pictures because I intend on adding some when things get going, so if it's simple that's great. Also, if you find any musical theatre pictures that don't include faces, are just bodies or feet, that would work as well.
Updates

The web address needs to be blstage.com. I have already purchased the domain name from WebNest. Let me know if there are any steps I might be missing or any other info I need to provide. Also, I need to be able to edit the website in the future but I'm not sure which format is best for that.

Target Market(s)

Theatre parents and students

Industry/Entity Type

Building

Requirements
Must have
• Stated above.

```html
<!DOCTYPE html>
<html lang="en">
<head>
<meta charset="utf-8">
<title>Bright Lantern Stage School — Registration</title>
<link href="https://fonts.googleapis.com/css2?family=Cormorant+Upright:wght@400;500&family=Italiana&display=swap" rel="stylesheet">
<style>
:root{
  --brand-red:#9b0000;
  --ink:#111111;
  --muted:#777777;
  --card-bg:#f4f4f4;
  --card-line:#d6d6d6;
  --rule:#cccccc;
  --go-top:#22ee22;
  --go-bottom:#00b800;
  --page:#ffffff;
}
*{box-sizing:border-box;margin:0;padding:0}
html,body{width:1200px;height:1000px;overflow:hidden;background:var(--page)}
body{font-family:"Cormorant Upright",Georgia,serif;color:var(--ink);position:relative;border-top:4px solid var(--brand-red);border-bottom:4px solid var(--brand-red)}
.site-header{position:absolute;top:0;left:0;width:1200px;height:150px}
.brand{position:absolute;left:262px;top:60px;display:flex;align-items:center;gap:10px;font-size:30px;color:var(--ink);font-family:"Italiana",serif}
.brand-mark{width:14px;height:14px;background:var(--brand-red)}
.main-nav{position:absolute;left:616px;top:66px;display:flex;gap:48px;font-size:24px;font-family:"Italiana",serif}
.main-nav a{color:var(--muted);text-decoration:none;padding-bottom:2px}
.main-nav a.current{color:var(--ink);border-bottom:2px solid var(--brand-red)}
.hero{position:absolute;left:100px;top:151px;width:1000px;height:131px;background:linear-gradient(90deg,#f2f2f2 0%,#c9c2bc 18%,#5a6478 40%,#b48a74 58%,#3d4c66 80%,#f4f4f4 100%);display:flex;align-items:center;justify-content:center}
.hero-title{font-family:"Italiana",serif;font-size:52px;color:#fff;font-weight:400;text-shadow:0 2px 6px rgba(0,0,0,.55)}
.classes{position:absolute;left:100px;top:306px;width:1000px;display:flex;gap:21px}
.class{width:319px;text-align:center}
.class-name{font-family:"Italiana",serif;font-style:italic;font-size:38px;font-weight:400;height:48px;line-height:44px}
.class-card{background:var(--card-bg);border:1px solid var(--card-line);border-radius:4px;height:424px;padding:12px 13px 0}
.age{font-size:23px;line-height:28px}
.dates{font-size:15px;line-height:18px}
.divider{border:0;border-top:1px solid var(--rule);margin:14px 0}
.day{font-size:22px;line-height:24px}
.time{font-size:29px;line-height:32px}
.info{font-size:15.5px;line-height:17.6px;text-align:left;height:104px;margin-top:18px}
.price{font-size:44px;line-height:50px;margin-top:18px}
.register{display:block;margin:12px auto 0;width:196px;height:38px;background:linear-gradient(var(--go-top),var(--go-bottom));color:#fff;font-family:"Italiana",serif;font-style:italic;font-size:27px;line-height:38px;text-decoration:none;box-shadow:0 2px 4px rgba(0,0,0,.3)}
.site-footer{position:absolute;left:100px;top:841px;width:1000px;border-top:1px solid var(--rule);height:150px;display:flex;justify-content:center;align-items:center}
.site-footer .brand{position:static}
</style>
</head>
<body>
<header class="site-header">
  <div class="brand"><span class="brand-mark"></span>Bright Lantern</div>
  <nav class="main-nav">
    <a href="#">Home</a>
    <a href="#" class="current">Registration</a>
    <a href="#">About</a>
  </nav>
</header>

<section class="hero" role="img" aria-label="Soft-focus photo of young performers in class">
  <h1 class="hero-title">Curriculums</h1>
</section>

<main class="classes">
  <article class="class">
    <h2 class="class-name">Moss Harbor</h2>
    <div class="class-card">
      <p class="age">4-6 Musical Theatre</p>
      <p class="dates">January 6th- February 24th (8 Weeks)</p>
      <hr class="divider">
      <p class="day">Tuesday's</p>
      <p class="time">4:00PM - 5:00PM</p>
      <hr class="divider">
      <p class="info">In MT 4-6 your students will learn the basics of singing, dancing, and acting. A lesson of theatre terminology or technique will be taught each week as well as working on the show that will be performed at the end of the 8 weeks semester.</p>
      <p class="price">160$</p>
      <a class="register" href="#">Register</a>
    </div>
  </article>
  <article class="class">
    <h2 class="class-name">Tilly</h2>
    <div class="class-card">
      <p class="age">6-9 Musical Theatre</p>
      <p class="dates">January 6th- February 24th (8 Weeks)</p>
      <hr class="divider">
      <p class="day">Tuesday's</p>
      <p class="time">5:15PM - 6:45PM</p>
      <hr class="divider">
      <p class="info">In MT 6-9 your students will learn the basics of singing, dancing, and acting. A lesson of theatre terminology or technique will be taught each week as well as working on the show that will be performed at the end of the 8 weeks semester.</p>
      <p class="price">220$</p>
      <a class="register" href="#">Register</a>
    </div>
  </article>
  <article class="class">
    <h2 class="class-name">Gilded</h2>
    <div class="class-card">
      <p class="age">9-12 Musical Theatre</p>
      <p class="dates">January 6th- February 24th (8 Weeks)</p>
      <hr class="divider">
      <p class="day">Wednesday's</p>
      <p class="time">5:00PM - 7:00PM</p>
      <hr class="divider">
      <p class="info">In MT 9-12 your students will learn the basics of singing, dancing, and acting. A lesson of theatre terminology or technique will be taught each week as well as working on the show that will be performed at the end of the 8 weeks semester.</p>
      <p class="price">240$</p>
      <a class="register" href="#">Register</a>
    </div>
  </article>
</main>

<footer class="site-footer">
  <div class="brand"><span class="brand-mark"></span>Bright Lantern</div>
</footer>
</body>
</html>
```